Vacation/Holiday Home Wordpress Website

I currently have a website for our vacation/holiday rental home. It is 6 years old and needs a complete redesign to acommodate many new features available today. The existing website can be seen at www.coralwindstays.co.uk . The purpose of the website is mainly to provide useful infomation about our home, the destination of Barbados. The customer is also able to check availability and book. Please note that there is a booking element to the website which is hosted externally. This can be seen at

http://stay.reservequick-hub.net/PickArrival_Mini.asp?ref=kTR%3DWQPA%26LMN%3DHXJX

I now wish to add key functionality such as:

- Video of property and area
- Customer video testimonials
- Other useful information

The navigation, menus and buttons need to be re designed to give a modern, innovative and professional look and feel.

My customers are mainly females between the ages of 35 and 55. The website needs to reassure customers who are parting with a lot of mony by booking online. It needs to give a sense of trust as this may be a once in a lifetime trip which they have saved up for for a long time. Many visitors to the website will be referred by other websites such as www.nestroam.co.uk and www.villaquarters.co.uk.
Updates

Dear designers, 

Thank you for taking the time to write some further comments to you all. 

1. The homepage should have an availability search function as a key feature

2. The look and feel does NOT need to have the 3 feature columns like my current website has

3.  There should not be too much text on the homepage. Brief text can be included with 'more'  buttons to reveal more information 

4.  For designs that are under consideration, we will need to see a design for the other pages as they will be different to the homepage. Information from other pages on the existing website can be used. 

Reason: Dear all, I will be providing extensive feedback later today following a review that we have conducted with a group of our guests. To enable you to read and use this information, we have extended the deadline by 5 days. Thank you for the design submisions so far. We hope that the additional feedback will enable you to amend your designs appropriately. Regards Martin Elswick

Dear all,

Thank you for your designs.  I apologise that I am unable to give detailed feedback on each and every design submitted.  I will contact you individually and indicate whether we would like you to submit any further designs.  These should take into account the feedback below.

Feedback from design review group

1.  Logo should not be displayed in a white box.  It should blend in with the background or be overlayed onto the picture.

2.  There must be an availability calendar on the home page.

3.  Any background image should be subtle, maybe blurred and not distract from the main area.

4.  Text should be limited to a few key words with a 'read more' button to reveal more information.

5.  A gallery/slide show should be featured in the top part of the screen

6.  Icons can be used as navigation buttons

7.  Video testimonials is a key feature and should appear on the home page

8.   The use of bold and vibrant colours is preferred

9.   The 3 column format of the old website should not be copied

Regards

Martin

Target Market(s)

Female's, Families, 35 to 55 year olds, travellers to Barbados

Industry/Entity Type

Online

Requirements
Must have
• Pictures
Video
Testimonials
Clear and stylish navigation
Easy to use navigation
Should not have
• Dated look or feel

```html
<!DOCTYPE html>
<html lang="en">
<head>
<meta charset="utf-8">
<title>Coral Wind Stays – Solmera Holiday Home</title>
<link rel="stylesheet" href="https://fonts.googleapis.com/css2?family=Source+Sans+3:wght@400;600;700&family=Roboto:ital,wght@0,400;1,400&display=swap">
<style>
:root{
  --sky-top:#2c8fd6;
  --sky-bottom:#62d7ea;
  --red:#e8341a;
  --red-dark:#c42406;
  --blue:#1760d6;
  --ink:#222;
  --body:#1a1a1a;
  --muted:#666;
  --card:#e7e7e7;
  --card-edge:#d6d6d6;
  --footer:#232323;
  --white:#fff;
}
*{box-sizing:border-box;margin:0;padding:0}
html,body{width:1115px;height:1200px;overflow:hidden}
body{background:linear-gradient(180deg,var(--sky-top) 0,#6cc6ee 180px,var(--sky-bottom) 600px);font-family:Arial,Helvetica,sans-serif}
.stage{position:relative;width:1200px;height:1291px;transform:scale(.92917);transform-origin:0 0}
.abs{position:absolute}
.page{left:102px;top:31px;width:996px;height:1150px;background:var(--white);border-radius:8px 8px 0 0}
.brand{left:113px;top:72px;display:flex;align-items:center;gap:12px;font-family:"Source Sans 3",sans-serif;font-weight:600;font-size:28px;letter-spacing:3px;color:var(--red)}
.brand-dot{width:22px;height:22px;border-radius:50%;background:var(--red)}
.contact{right:130px;top:68px;text-align:right;font-family:"Source Sans 3",sans-serif}
.contact-lead{font-size:19px;color:var(--blue);line-height:24px}
.contact-row{display:flex;align-items:flex-start;gap:8px;justify-content:flex-end}
.contact-row svg{margin-top:4px;flex:none}
.contact-phone{font-family:Roboto,sans-serif;font-size:35px;color:#333;letter-spacing:-1.5px;line-height:38px}
.contact-mail{font-size:16px;color:var(--red);line-height:18px}
.nav-tab{top:150px;width:28px;height:88px;background:var(--red-dark);border-radius:6px}
.nav{left:92px;top:168px;width:1015px;height:52px;background:linear-gradient(180deg,#f0501f,#e02c06);border-radius:4px;display:flex;align-items:center;padding-left:22px;font-family:"Source Sans 3",sans-serif;font-weight:600;font-size:14.5px;color:var(--white)}
.nav a{color:inherit;text-decoration:none;padding:0 28px;border-right:1px solid #f3774f;line-height:32px}
.nav a:last-child{border-right:none}
.nav a.is-active{border:1px solid #b71e03;background:#d8300a;border-radius:4px;box-shadow:inset 0 1px 3px rgba(0,0,0,.35);padding:0 21px;margin-right:8px}
.hero{left:107px;top:226px;width:986px;height:361px;background:linear-gradient(90deg,#2fb4d9 0,#7fd8e8 25%,#cfe7ea 55%,#e9dcc6 100%)}
.search{left:171px;top:283px;width:436px;height:232px;background:var(--white);border-radius:10px 0 0 10px;box-shadow:0 2px 8px rgba(0,0,0,.25);padding:8px 17px;font-family:"Source Sans 3",sans-serif}
.search-title{font-size:32px;font-weight:400;color:var(--red);letter-spacing:.5px}
.search-title b{color:var(--blue);font-weight:700}
.field{position:absolute;border:1px solid #c9c9c9;background:var(--white);font-size:14px;color:#444;padding-left:7px;display:flex;align-items:center;font-family:Arial,sans-serif}
.field-btn{position:absolute;background:linear-gradient(180deg,#3da0f5,#1675d8);color:var(--white);font-weight:700;font-size:14.5px;display:flex;align-items:center;justify-content:center}
.cal{position:absolute;right:4px;top:4px;width:18px;height:16px;border:1px solid #bbb;border-top:4px solid #e04a3a;border-radius:2px}
.caret{position:absolute;right:2px;top:2px;width:18px;height:20px;background:#111}
.caret:after{content:"";position:absolute;left:5px;top:8px;border:4px solid transparent;border-top:5px solid var(--white)}
.label{position:absolute;font-size:15px;font-weight:600;color:#333;letter-spacing:.3px}
.photo-frame{left:606px;top:255px;width:427px;height:290px;background:var(--white);border:1px solid #ddd;padding:7px}
.photo{width:100%;height:100%;background:linear-gradient(180deg,#4a78c9 0,#8fb0e0 35%,#c9b79a 55%,#4f8f3a 75%,#6aa84b 100%)}
.newsletter{left:138px;top:573px;width:924px;height:82px;background:linear-gradient(180deg,#f2f2f2,#fff);border:1px solid #e6e6e6;border-top:none}
.newsletter-title{left:188px;top:590px;font-family:"Source Sans 3",sans-serif;font-size:28px;color:var(--red)}
.newsletter-title b{color:var(--blue);font-weight:600}
.news-input{left:437px;top:592px;width:432px;height:33px;border:1px solid #ccc;background:var(--white);font-style:italic;font-size:13px;color:#777;padding-left:11px;display:flex;align-items:center}
.news-btn{left:869px;top:592px;width:120px;height:33px;background:var(--red);color:var(--white);font-family:"Source Sans 3",sans-serif;font-size:21px;display:flex;align-items:center;justify-content:center}
.intro{left:121px;top:680px;width:648px;color:var(--body)}
.intro h1{font-family:"Source Sans 3",sans-serif;font-size:23px;font-weight:600;color:var(--ink);letter-spacing:.5px;margin-bottom:18px}
.intro p{font-size:13px;line-height:20px;margin-bottom:20px}
.video{left:791px;top:676px;width:278px;height:216px;background:#111;padding:7px 6px 0;box-shadow:0 10px 14px -8px rgba(0,0,0,.35)}
.video-screen{width:266px;height:177px;background:linear-gradient(135deg,#f1e8cf,#dfe6d8 55%,#9bc3d8);position:relative}
.play{position:absolute;left:103px;top:67px;width:60px;height:42px;background:#222;border-radius:3px}
.play:after{content:"";position:absolute;left:22px;top:9px;border-left:20px solid var(--white);border-top:12px solid transparent;border-bottom:12px solid transparent}
.video-bar{position:absolute;left:0;bottom:0;width:278px;height:32px;background:linear-gradient(180deg,#f4f4f4,#d2d2d2);font-size:6px;color:#555;padding:3px 6px;font-family:Arial,sans-serif}
.video-track{position:absolute;left:30px;top:8px;width:210px;height:3px;background:#999}
.video-track:before{content:"";position:absolute;left:0;top:0;width:70px;height:3px;background:#333}
.video-labels{position:absolute;left:6px;bottom:3px;right:6px;display:flex;justify-content:space-between}
.rule{left:121px;top:925px;width:959px;border-top:1px dotted #aaa}
.section-title{left:120px;top:948px;font-family:"Source Sans 3",sans-serif;font-size:28px;color:var(--red)}
.section-title b{color:var(--blue);font-weight:600}
.testimonial{top:1002px;width:461px;height:112px;background:var(--card);border:3px solid var(--card-edge);border-radius:9px}
.testimonial-tail{top:1113px;width:0;height:0;border-left:14px solid transparent;border-right:8px solid transparent;border-top:22px solid var(--card-edge)}
.avatar{position:absolute;left:11px;top:13px;width:82px;height:78px;background:linear-gradient(180deg,#d9d9d9,#9a9a9a);border:3px solid var(--white);border-radius:6px}
.quote{position:absolute;left:108px;top:14px;width:336px;font-family:Roboto,sans-serif;font-style:italic;font-size:12.5px;line-height:15.8px;color:#4c4c4c}
.credit{top:1130px;font-family:Roboto,sans-serif;font-size:12px;color:var(--muted)}
.credit b{color:#0c4fb0;font-weight:700;margin-right:8px}
.credit:before{content:"";display:inline-block;margin-right:5px;border-left:6px solid #5fb82d;border-top:5px solid transparent;border-bottom:5px solid transparent}
.footer-line{left:0;top:1180px;width:1200px;height:8px;background:#f41a0a}
.footer{left:0;top:1188px;width:1200px;height:103px;background:var(--footer)}
.footer-brand{left:105px;top:1236px;display:flex;align-items:center;gap:10px;font-family:"Source Sans 3",sans-serif;font-size:21px;letter-spacing:3px;color:#9a9a9a}
.footer-brand .brand-dot{width:16px;height:16px;background:#9a9a9a}
.footer-links{right:110px;top:1213px;text-align:right;font-family:Roboto,sans-serif;font-size:12.5px;letter-spacing:.6px;color:#eee;line-height:24px}
.footer-links span{margin:0 5px;color:#bbb}
</style>
</head>
<body>
<div class="stage">
  <div class="abs page"></div>

  <div class="abs brand"><span class="brand-dot"></span>CORAL WIND STAYS</div>

  <div class="abs contact">
    <div class="contact-lead">For Appointment Call Us Today</div>
    <div class="contact-row">
      <svg width="28" height="46" viewBox="0 0 28 46" aria-hidden="true">
        <rect x="1" y="6" width="26" height="38" rx="3" fill="#222"/>
        <rect x="18" y="0" width="4" height="8" fill="#222"/>
        <rect x="5" y="10" width="18" height="9" fill="#fff"/>
        <g fill="#fff"><rect x="5" y="23" width="4" height="3"/><rect x="12" y="23" width="4" height="3"/><rect x="19" y="23" width="4" height="3"/><rect x="5" y="29" width="4" height="3"/><rect x="12" y="29" width="4" height="3"/><rect x="19" y="29" width="4" height="3"/><rect x="5" y="35" width="4" height="3"/><rect x="12" y="35" width="4" height="3"/><rect x="19" y="35" width="4" height="3"/></g>
      </svg>
      <div>
        <div class="contact-phone">044 765 2190</div>
        <div class="contact-mail">hello@coralwindstays.com</div>
      </div>
    </div>
  </div>

  <div class="abs nav-tab" style="left:92px"></div>
  <div class="abs nav-tab" style="left:1079px"></div>
  <nav class="abs nav">
    <a class="is-active">HOME</a>
    <a>SOLMERA HOLIDAY HOME</a>
    <a>LOCAL AREA</a>
    <a>BOOK NOW</a>
    <a>PRICES</a>
    <a>TESTIMONIALS</a>
    <a>CONTACT US</a>
  </nav>

  <div class="abs hero" role="img" aria-label="Blurred tropical beach with turquoise sea and palm trees"></div>

  <div class="abs search">
    <div class="search-title">Solmera <b>Availability</b></div>
    <div class="field" style="left:17px;top:55px;width:290px;height:32px">Where are you going?</div>
    <div class="field-btn" style="left:306px;top:55px;width:115px;height:32px">Search Now</div>
    <div class="field" style="left:23px;top:115px;width:107px;height:25px">dd/mm/yy<span class="cal"></span></div>
    <div class="field" style="left:171px;top:115px;width:107px;height:25px">dd/mm/yy<span class="cal"></span></div>
    <div class="label" style="left:23px;top:158px">Bedrooms</div>
    <div class="label" style="left:173px;top:158px">Sleeps</div>
    <div class="field" style="left:23px;top:186px;width:107px;height:25px">Any<span class="caret"></span></div>
    <div class="field" style="left:173px;top:186px;width:107px;height:25px">Any<span class="caret"></span></div>
  </div>

  <div class="abs photo-frame"><div class="photo" role="img" aria-label="Photo of the holiday home exterior with lawn and driveway"></div></div>

  <div class="abs newsletter"></div>
  <div class="abs newsletter-title">Sign Up <b>Newsletter:</b></div>
  <div class="abs news-input">Email Address</div>
  <div class="abs news-btn">Sign Up</div>

  <section class="abs intro">
    <h1>Solmera - A two bedroomed, fully air-conditioned.</h1>
    <p>This stunning, semi-detached, spacious (1400 square feet) two bedroom, three bathroom house offers the ultimate in luxury and accommodates a maximum of 4 people The house is air-conditioned upstairs, the spacious living area seats five in comfort.</p>
    <p>The living area boasts a full range of entertainment equipment including satellite/cable television, DVD player, CD stereo and radio. The dining area provides comfortable seating for 4 people. The master bedroom is well equipped with a king sized bed, bedside tables, lamps more than ample wardrobe space</p>
  </section>

  <div class="abs video">
    <div class="video-screen" role="img" aria-label="Video still of a bright bedroom with a large bed and window">
      <span class="play"></span>
    </div>
    <div class="video-bar">
      <span>01:46</span><span style="float:right">02:28</span>
      <span class="video-track"></span>
      <div class="video-labels"><span>Pause</span><span>email · link · code</span><span>Menu</span></div>
    </div>
  </div>

  <div class="abs rule"></div>
  <div class="abs section-title">Client <b>Testimonials</b></div>

  <div class="abs testimonial" style="left:124px">
    <div class="avatar" role="img" aria-label="Guest portrait"></div>
    <p class="quote">Aenean sed nulla mattis augue pulvinar varius. Pletesque habitant morbi tristique senectus et netus et malesuada fames ac turpis egestas. Vestibulum pharetra sapien a libero congue sed porta nulla sodales.Pellentesqu abitant lesuada fames ac turpis egestas.</p>
  </div>
  <div class="abs testimonial-tail" style="left:140px"></div>
  <div class="abs credit" style="left:166px"><b>Rowan Tilley,</b>Maven. Co-Creator of Lumen Notes</div>

  <div class="abs testimonial" style="left:618px">
    <div class="avatar" role="img" aria-label="Guest portrait"></div>
    <p class="quote">Aenean sed nulla mattis augue pulvinar varius. Peetesque habitant morbi tristique senectus et netus et malesuada fames ac turpis egestas. Vestibulum pharetra sapien a libero congue sed porta nulla sodales.Pellentesqu abitant lesuada fames ac turpis egestas.</p>
  </div>
  <div class="abs testimonial-tail" style="left:634px"></div>
  <div class="abs credit" style="left:660px"><b>Rowan Tilley,</b>Maven. Co-Creator of Lumen Notes</div>

  <div class="abs footer-line"></div>
  <footer class="abs footer"></footer>
  <div class="abs footer-brand"><span class="brand-dot"></span>CORAL WIND STAYS</div>
  <div class="abs footer-links">
    <div>Home <span>~</span> Solmera Holiday Home <span>~</span> Local Area <span>~</span> Book Now <span>~</span> Prices <span>~</span> Testimonials <span>~</span> Contact us</div>
    <div>Coral Wind Stays, Copyright © 2013, Privacy Policy</div>
  </div>
</div>
</body>
</html>
```